Professional Learning Organization for Educators needs a Design Thinking Workshop Flyer

We need a flyer for a series of Introductory Design Thinking workshops we're delivering for education leaders.

We have generated our own version of the flyer with a word template, but want it to look even more professional and eye catching. It is attached.

We had an image that we thought might be good, but pulled it out so we don't bias designers' thinking.
Updates

Reason: We are a bit flexible on the deadline since this is a holiday week and people are traveling

Target Market(s)

Very busy education leaders whose curiosity needs to be stimulated enough to enroll in the course

Industry/Entity Type

Education

Font styles to use
Other font styles liked:
• Century Gothic or something closer to that

Requirements
Must have
• Some version of the text that is on the current flyer that I attached.
Nice to have
• I am very flexible and open right now on this design.

```html
<!DOCTYPE html>
<html lang="en">
<head>
<meta charset="utf-8">
<title>Design Thinking Workshops</title>
<link href="https://fonts.googleapis.com/css2?family=Didact+Gothic&family=Montserrat:wght@500;600;700&display=swap" rel="stylesheet">
<style>
  :root {
    --teal: #17b3c5;
    --orange: #f47b20;
    --ink: #1f1f1f;
    --body: #333333;
    --white: #ffffff;
    --rule: #c9c9c9;
  }
  * { box-sizing: border-box; margin: 0; padding: 0; }
  html, body { width: 720px; height: 1200px; overflow: hidden; background: var(--white); }
  .flyer {
    position: relative; width: 720px; height: 1200px; overflow: hidden;
    font-family: "Didact Gothic", "Century Gothic", sans-serif; color: var(--body);
  }
  .backdrop { position: absolute; inset: 0; }

  /* Left column */
  .intro { position: absolute; left: 22px; top: 615px; width: 400px; }
  .eyebrow { font-family: "Montserrat", sans-serif; font-weight: 500; color: var(--orange); font-size: 25px; letter-spacing: 0.5px; line-height: 1; }
  .title { font-family: "Montserrat", sans-serif; font-weight: 700; color: var(--orange); font-size: 50px; letter-spacing: 1.5px; line-height: 1.05; margin-top: 6px; }
  .title-rule { height: 1px; background: var(--rule); margin: 10px 0 22px; }
  .tagline { font-family: "Montserrat", sans-serif; font-weight: 600; color: var(--ink); font-size: 21px; line-height: 1.2; }
  .lead { font-size: 12.5px; line-height: 1.4; margin-top: 14px; text-align: justify; }
  .outcomes { list-style: none; margin: 20px 0 0 38px; font-size: 12.5px; line-height: 1.35; }
  .outcomes li { position: relative; margin-bottom: 9px; }
  .outcomes li::before { content: ""; position: absolute; left: -13px; top: 6px; width: 5px; height: 5px; border-radius: 50%; background: var(--orange); }
  .offer { color: var(--orange); font-size: 14px; line-height: 1.35; margin-top: 22px; text-align: justify; }
  .schedule { margin-top: 22px; width: 400px; font-size: 12.5px; }
  .session { display: flex; align-items: center; height: 19px; }
  .session-bar { width: 38px; height: 11px; background: var(--teal); margin-right: 12px; }
  .session-time { flex: 1; }
  .session-dates { width: 130px; word-spacing: 4px; }

  /* Right column */
  .testimonials { position: absolute; left: 440px; top: 440px; width: 280px; color: var(--white); }
  .testimonials-heading { font-family: "Montserrat", sans-serif; font-weight: 500; font-size: 24px; line-height: 1.35; text-align: right; padding-right: 12px; }
  .quote {
    position: relative; margin: 0 16px 0 16px; border: 1px solid rgba(255,255,255,0.85);
    text-align: center; font-size: 15px; line-height: 1.32; padding: 18px 14px 18px;
  }
  .quote + .quote { margin-top: 40px; }
  .quote-mark { position: absolute; left: 50%; transform: translateX(-50%); background: var(--teal); font-family: Georgia, serif; font-size: 34px; line-height: 1; padding: 0 5px; height: 22px; overflow: hidden; }
  .quote-mark.open { top: -12px; }
  .quote-mark.close { bottom: -14px; }
  .quotes { margin-top: 50px; }

  .enroll { position: absolute; left: 440px; top: 1036px; width: 280px; height: 50px; background: var(--orange); color: var(--white); font-family: "Montserrat", sans-serif; font-weight: 500; font-size: 26px; display: flex; align-items: center; padding-left: 12px; white-space: nowrap; }
  .enroll-word { background: var(--white); color: var(--ink); font-weight: 600; padding: 0 5px; margin-left: 6px; line-height: 1.25; }
  .learn-more { position: absolute; left: 452px; top: 1094px; color: var(--ink); font-family: "Montserrat", sans-serif; font-weight: 600; font-size: 13.5px; }
  .learn-more .url { color: var(--white); }
  .fine-print { position: absolute; left: 452px; top: 1130px; width: 255px; color: var(--ink); font-size: 12px; line-height: 1.3; text-align: justify; }
  .fine-print strong { color: var(--orange); font-weight: 400; }
</style>
</head>
<body>
<div class="flyer">
  <svg class="backdrop" width="720" height="1200" viewBox="0 0 720 1200">
    <defs>
      <linearGradient id="classroomTones" x1="0" y1="0" x2="1" y2="1">
        <stop offset="0" stop-color="#c9a48e"/>
        <stop offset="0.35" stop-color="#e2d6c8"/>
        <stop offset="0.65" stop-color="#6f88a8"/>
        <stop offset="1" stop-color="#5a3b30"/>
      </linearGradient>
    </defs>
    <rect x="0" y="0" width="720" height="620" fill="url(#classroomTones)" role="img" aria-label="Photo of a smiling teacher drawing with young children at a classroom table covered in crayons"/>
    <path d="M0,545 Q430,620 720,205 L720,1200 L0,1200 Z" fill="var(--teal)"/>
    <path d="M0,592 Q260,602 440,572 L440,1200 L0,1200 Z" fill="var(--white)"/>
  </svg>

  <section class="intro">
    <div class="eyebrow">DESIGN THINKING</div>
    <h1 class="title">WORKSHOPS</h1>
    <div class="title-rule"></div>
    <h2 class="tagline">Designing your way to better solutions.</h2>
    <p class="lead">Meadowbrook Public Schools and Ridgeline Educational Services invite you to discover the power of Design Thinking. During our three session course, you will learn and practice mindsets and tools that help you continuously and creatively improve the experiences of the people you serve by:</p>
    <ul class="outcomes">
      <li>Understanding what your teachers, students and community truly need in their learning and work experiences</li>
      <li>Designing solutions that better meet their needs</li>
      <li>Seeking authentic feedback and reactions to these solutions prior to their implementation.</li>
    </ul>
    <p class="offer">We are offering this three-session course at four different times in spring semester. Please choose the course that works best for your schedule.</p>
    <div class="schedule">
      <div class="session"><span class="session-bar"></span><span class="session-time">Monday mornings:</span><span class="session-dates">1/23, 1/30 and 2/6</span></div>
      <div class="session"><span class="session-bar"></span><span class="session-time">Tuesday afternoons:</span><span class="session-dates">2/07, 2/14 and 2/21</span></div>
      <div class="session"><span class="session-bar"></span><span class="session-time">Wednesday afternoons:</span><span class="session-dates">3/08, 3/15 and 3/22</span></div>
      <div class="session"><span class="session-bar"></span><span class="session-time">Wednesday evenings:</span><span class="session-dates">2/08, 2/15 and 2/22</span></div>
    </div>
  </section>

  <section class="testimonials">
    <h2 class="testimonials-heading">What our<br>participants say…</h2>
    <div class="quotes">
      <blockquote class="quote"><span class="quote-mark open">“</span>This has been an empowering experience that allowed me to try out dramatic changes in my practice that I wouldn’t have imagined before.<span class="quote-mark close">”</span></blockquote>
      <blockquote class="quote"><span class="quote-mark open">“</span>I never realized how often I’ve guessed and assumed what our teachers and students need – now I have a way to stop guessing!<span class="quote-mark close">”</span></blockquote>
      <blockquote class="quote"><span class="quote-mark open">“</span>I finally have tools to generate truly creative ideas that people actually embrace…because they meet their needs<span class="quote-mark close">”</span></blockquote>
    </div>
  </section>

  <div class="enroll">Click here to <span class="enroll-word">Enroll.</span></div>
  <p class="learn-more">Go to <span class="url">www.ridgelinelearning.org</span> to learn more.</p>
  <p class="fine-print">This course is held in <strong>Meadowbrook Public Schools.</strong> No fee for MPS leaders. $150 fee for leaders outside of MPS.</p>
</div>
</body>
</html>
```